Harbor Mortgage Relief

Please help us give our website a remake or a FACELIFT. It is not very good but it says what we need it to say. But the design is terrible.
I would like our new design font and logo to be used as the theme.

I also want more photos on the site.

I also want consistency with the pages so they look clean.

We want the professionals to do this, let's see what you got!

Thank you!
Updates

Project Deadline Extended
Reason: I can understand you want to be paid. So I will commit to the fee but I want you to have time to make a KICK ASS website for me dudes! Thanks

HI!  Just wanted to say thanks for your time on these.  A lot are great.  However the firefighters have nothing to do with Foreclosure.  We are saving peoples homes from the bank taking them and selling them.   I LOVE the house photos and the families on the website.  That is the direction we like.  THanks.

THANK U ALL FOR THE WORK!   I like a few ending in the numbers: 147  733  693  536  620  478  727  508     I will go over them and choose one soon.  Thank you.   You will be paid shortly. 

Requirements
Must have
• Bright, Upbeat photos. Color scheme should be in order. We like icons on the bottom. not just text.

```html
<!DOCTYPE html>
<html lang="en">
<head>
<meta charset="utf-8">
<title>Harbor Mortgage Relief</title>
<link href="https://fonts.googleapis.com/css2?family=Ubuntu:wght@400;500;700&family=Open+Sans:wght@400;600&display=swap" rel="stylesheet">
<style>
:root{
  --navy:#0f4c84;
  --navy-dark:#0b3f70;
  --nav:#1b5f9b;
  --nav-dark:#14548c;
  --link:#1f5f98;
  --text:#3a3a3a;
  --orange:#f29a0c;
  --orange-dark:#d98200;
  --hero-bg:#f1f2f4;
  --footer-bg:#eaeef3;
  --field:#e9eff6;
  --field-border:#c9d6e4;
  --white:#ffffff;
}
*{margin:0;padding:0;box-sizing:border-box}
html,body{width:1103px;height:1200px;overflow:hidden;background:var(--white)}
body{position:relative;font-family:"Open Sans",Arial,sans-serif;color:var(--text)}
.abs{position:absolute}
.heading{font-family:"Ubuntu",Arial,sans-serif}

/* header */
.site-header{left:0;top:0;width:1103px;height:129px;border-top:4px solid var(--navy-dark);background:linear-gradient(#fff,#eef0f3)}
.brand-name{left:44px;top:48px;font:500 25px "Ubuntu",Arial,sans-serif;color:var(--navy);letter-spacing:.2px}
.brand-slogan{left:244px;top:80px;font:400 14px "Ubuntu",Arial,sans-serif;color:var(--link)}
.call-label{left:870px;top:51px;font:400 18px "Ubuntu",Arial,sans-serif;color:var(--navy)}
.call-number{left:870px;top:70px;font:500 27px "Ubuntu",Arial,sans-serif;color:var(--navy)}

/* nav */
.main-nav{left:0;top:129px;width:1103px;height:54px;background:linear-gradient(var(--nav) 50%,var(--nav-dark) 50%)}
.main-nav a{position:absolute;top:17px;font:400 14px "Open Sans",Arial,sans-serif;color:#e6eef7;text-decoration:none}
.main-nav a.current{font-weight:600;color:#fff}
.nav-sep{position:absolute;top:0;width:1px;height:54px;background:rgba(255,255,255,.18)}

/* hero */
.hero{left:0;top:183px;width:1103px;height:324px;background:linear-gradient(#f7f7f8,var(--hero-bg))}
.hero-title{left:84px;top:57px;font:500 28px "Ubuntu",Arial,sans-serif;color:var(--navy)}
.hero-punch{left:84px;top:94px;font:400 22px "Ubuntu",Arial,sans-serif;color:var(--navy)}
.hero-text{left:84px;top:128px;width:400px;font:400 13px/21.5px "Ubuntu",Arial,sans-serif;color:#444}
.btn{display:flex;align-items:center;justify-content:center;gap:7px;background:linear-gradient(var(--orange),var(--orange-dark));color:#fff;border-radius:5px;box-shadow:0 2px 3px rgba(0,0,0,.2);font-family:"Ubuntu",Arial,sans-serif}
.hero-btn{left:84px;top:208px;width:114px;height:35px;font-size:15px}
.hero-frame{left:521px;top:18px;width:513px;height:286px;background:#fff;border-radius:4px;box-shadow:0 1px 6px rgba(0,0,0,.2)}
.hero-photo{position:absolute;left:6px;top:6px;width:501px;height:274px;background:linear-gradient(#a9cdea 0%,#d9e6ee 38%,#b99a7c 60%,#7fa35a 86%,#5f8a3e 100%)}
.hero-arrow{top:102px}

/* welcome */
.welcome-title{left:33px;top:530px;font:400 20px "Ubuntu",Arial,sans-serif;color:var(--navy)}
.welcome-title strong{font-weight:500}
.welcome-body{left:33px;top:563px;width:725px;font-size:11.4px;line-height:18.3px;color:#3c3c3c}
.welcome-body p{margin-bottom:18.3px}

/* contact form */
.contact-form{left:777px;top:520px;width:306px;height:378px;border:1px solid #c6d3e2;border-radius:6px;background:#fff}
.form-title{position:absolute;left:0;top:0;width:100%;height:41px;padding:10px 18px;border-bottom:1px solid #c6d3e2;background:linear-gradient(#fff,#f1f5f9);border-radius:6px 6px 0 0;font:400 20px "Ubuntu",Arial,sans-serif;color:var(--navy)}
.field{position:absolute;width:271px;height:30px;background:var(--field);border:1px solid var(--field-border);border-radius:5px;padding:7px 11px;font-size:11.5px;color:var(--navy)}
.field.message{height:110px}
.submit-btn{left:22px;top:326px;width:106px;height:31px;font:600 12px "Open Sans",Arial,sans-serif}

/* footer */
.site-footer{left:0;top:926px;width:1103px;height:226px;background:var(--footer-bg)}
.footer-sep{position:absolute;top:2px;width:1px;height:176px;background:#cfd6de}
.footer-title{position:absolute;top:20px;font:500 20px "Ubuntu",Arial,sans-serif;color:var(--navy)}
.footer-link{position:absolute;font-size:12px;color:var(--link)}
.social-icon{position:absolute;width:22px;height:22px;border-radius:3px;background:linear-gradient(#4a8fd0,#2a69a8)}
.contact-line{position:absolute;left:604px;font:400 14px "Ubuntu",Arial,sans-serif;color:var(--navy)}
.contact-line.name{font-size:16px}
.bottom-bar{left:0;top:1152px;width:1103px;height:48px;background:#fff}
.copyright{position:absolute;left:36px;top:15px;font-size:11.5px;color:var(--link)}
</style>
</head>
<body>

<header class="abs site-header">
  <div class="abs brand-name">HARBOR MORTGAGE RELIEF</div>
  <div class="abs brand-slogan">your slogan line here..</div>
  <div class="abs call-label">Call Us Now</div>
  <div class="abs call-number">877-555-0148</div>
</header>

<nav class="abs main-nav">
  <a class="current" href="#" style="left:51px">Main</a>
  <span class="nav-sep" style="left:112px"></span>
  <a href="#" style="left:148px">About Us</a>
  <span class="nav-sep" style="left:236px"></span>
  <a href="#" style="left:270px">Services</a>
  <span class="nav-sep" style="left:350px"></span>
  <a href="#" style="left:385px">Contact Us</a>
  <span class="nav-sep" style="left:480px"></span>
  <a href="#" style="left:517px">Financing Options</a>
</nav>

<section class="abs hero">
  <svg class="abs hero-arrow" style="left:23px" width="26" height="80" viewBox="0 0 26 80"><polyline points="24,2 2,40 24,78" fill="none" stroke="#2f6aa3" stroke-width="1.6"/></svg>
  <svg class="abs hero-arrow" style="left:1053px" width="26" height="80" viewBox="0 0 26 80"><polyline points="2,2 24,40 2,78" fill="none" stroke="#2f6aa3" stroke-width="1.6"/></svg>
  <h1 class="abs hero-title">Harbor Mortgage Relief</h1>
  <h2 class="abs hero-punch">Punch line here goes here</h2>
  <p class="abs hero-text">Brightline Web Studio is a web service company, offering a wide range of services which range from designing and development, that is covering almost all the fields in the best possible way.</p>
  <a class="abs btn hero-btn">learn more <span>&#8250;</span></a>
  <div class="abs hero-frame">
    <div class="hero-photo" role="img" aria-label="Smiling family of four standing in front of their brick suburban home on a sunny day"></div>
  </div>
</section>

<h2 class="abs welcome-title">Welcome to &nbsp;<strong>HARBOR MORTGAGE RELIEF</strong></h2>
<div class="abs welcome-body">
  <p>HARBOR MORTGAGE RELIEF specializes in assisting homeowners who are in FORECLOSURE, by offering solid alternatives to losing your home in a Trustee Sale. Having your home foreclosed on can damage your credit for up to 7 years. Most foreclosures end with the home owner being evicted from their home, leaving them with no money, no place to live and without ample time to safely remove their possessions from their home. There is no need to have this happen to you. No matter what part of foreclosure process you are in, WE CAN HELP!</p>
  <p>If you have received a Notice of Default (NOD) or Notice of Trustee Sale (NTS), you have options. Contact us today to speak to one of our licensed specialist, and let us help you put this situation behind you.<br>We speak to hundreds of homeowners every day, we understand how frustrating this can be. Don't live in fear of what is to come. You have other options, please call or email us today and we will immediately put our specialist to work finding you a solution.</p>
  <p>Don't try to handle this frustrating situation by yourself. HARBOR MORTGAGE RELIEF is a team of knowledgeable real estate professionals, we can offer you a better solution during this tough time.<br>HARBOR MORTGAGE RELIEF has been assisting families in foreclosure for years. Our skill and integrity has earned us a reputation for fast, professional, courteous and thorough solutions. With over 50 years of real estate knowledge and experience HARBOR MORTGAGE RELIEF is ready to assist you.</p>
</div>

<aside class="abs contact-form">
  <div class="form-title">Contact Form</div>
  <div class="field" style="left:15px;top:57px">type your full name</div>
  <div class="field" style="left:17px;top:104px">type your phone no.</div>
  <div class="field" style="left:20px;top:151px">type your email address</div>
  <div class="field message" style="left:20px;top:199px">type your message</div>
  <a class="abs btn submit-btn">SUBMIT NOW <span>&#8250;</span></a>
</aside>

<footer class="abs site-footer">
  <h3 class="footer-title" style="left:42px">Quick links</h3>
  <a class="footer-link" style="left:43px;top:64px">Main Page</a>
  <a class="footer-link" style="left:43px;top:94px">About Our Company</a>
  <a class="footer-link" style="left:43px;top:124px">Services</a>
  <a class="footer-link" style="left:43px;top:155px">Financing Options</a>
  <a class="footer-link" style="left:187px;top:65px">FAQ's</a>
  <a class="footer-link" style="left:187px;top:95px">Contact Form</a>
  <a class="footer-link" style="left:187px;top:125px">Contact Us</a>

  <span class="footer-sep" style="left:307px"></span>

  <h3 class="footer-title" style="left:351px">Get in Touch</h3>
  <span class="social-icon" style="left:351px;top:62px"></span>
  <a class="footer-link" style="left:385px;top:65px">Connect with Chatterline</a>
  <span class="social-icon" style="left:351px;top:92px"></span>
  <a class="footer-link" style="left:385px;top:95px">Get in touch with Friendwall</a>
  <span class="social-icon" style="left:351px;top:122px"></span>
  <a class="footer-link" style="left:385px;top:125px">Stay on Friendwall</a>
  <span class="social-icon" style="left:351px;top:152px"></span>
  <a class="footer-link" style="left:385px;top:155px">Connect with Searchly</a>

  <span class="footer-sep" style="left:568px"></span>

  <h3 class="footer-title" style="left:603px">Contact Info</h3>
  <div class="contact-line name" style="top:59px">HARBOR MORTGAGE RELIEF</div>
  <div class="contact-line" style="top:93px">118 Harbor View Drive, Suite 210</div>
  <div class="contact-line" style="top:118px">Bayport, CA 90210</div>
  <div class="contact-line" style="top:143px">877-555-0148</div>
</footer>

<div class="abs bottom-bar">
  <div class="copyright">© 2012 Company Name &nbsp;|&nbsp; All right reserved</div>
</div>

</body>
</html>
```